Plumbing and Fire Protection Consulting Engineering

Business Cards for one person plumbing and fire protection engineering consulting business based in NJ, serving mostly New York City:
Ravel Consulting, Plumbing and Fire Protection Engineering
Martin Kolbeck- President
52-07 Danforth Street, Harlow Glen, HG 07563
201-486-2713
ravelpipework@ravelmail.example

Target Market(s)

- Private Building Developers, looking to reduce construction cost
- MEP (Mechanical, Electrical, Plumbing) Design Engineers that have staff shortage, need temporary help, advise, drawings quality control
- Architects that need advise on plumbing or fire protection
- Any of the above that need opinion on disputed construction costs, change orders, construction observation reports

Industry/Entity Type

Business

Contact Information for Business Card

Logo and business card should include (other suggestions welcome):
- A plumbing symbol, like pipe or wrench or similar
- Fire Protection symbol, like fire sprinkler
- Dollar signs $$$$$ in descending font sizes suggesting construction cost reduction as a result of my work. or some other symbol of economic design
- Symbol of engineering
- High rise building(s) or Manhattan skyline on the background, maybe building under construction.
- Maybe a building floor plan design (preferably old, not modern, like in Michelangelo or Gaudi sketches)

Font styles to use
Sans Serif

Colors

Designer to choose colors to be used in the design.

Requirements
Must have
• A card that is unique, unlike any others- like my business is.
• My name, business name, address, phone, email, see description
Nice to have
• Something that suggests 30+ years experience in this field, not sure how to convey this message.
• Maybe my Linkedin picture with Statue of Liberty on the background (attached) is good to have, but i am not sure- not insisting on that.
Should not have
• Symbols that not related to engineering design and construction- like fire truck, funny plumbers figures and symbols, toilets, etc.
• Computer symbols. I am not trying to impress clients with my computer skills, not my selling point

```html
<!DOCTYPE html>
<html lang="en">
<head>
<meta charset="utf-8">
<title>Ravel Consulting — Business Cards</title>
<link rel="stylesheet" href="https://fonts.googleapis.com/css2?family=Oswald:wght@700&family=PT+Sans:wght@400;700&display=swap">
<style>
  :root {
    --brand-blue: #1565b0;
    --brand-orange: #ec7a14;
    --card-white: #ffffff;
    --stage: #e9e6e1;
    --text-white: #ffffff;
  }
  * { box-sizing: border-box; margin: 0; padding: 0; }
  html, body { width: 1200px; height: 900px; overflow: hidden; }
  body {
    background: var(--stage);
    font-family: "PT Sans", Arial, sans-serif;
    position: relative;
  }
  .card {
    position: absolute;
    width: 525px;
    height: 300px;
    overflow: hidden;
    box-shadow: 0 6px 18px rgba(0,0,0,0.18);
  }
  /* back side */
  .card-back {
    left: 120px;
    top: 110px;
    background: var(--brand-blue);
    display: flex;
    align-items: center;
    justify-content: center;
    gap: 14px;
  }
  .card-back .mark-dot {
    width: 34px; height: 34px; border-radius: 50%;
    background: var(--text-white);
  }
  .card-back .wordmark {
    font-family: "Oswald", Impact, sans-serif;
    font-weight: 700;
    font-size: 40px;
    color: var(--text-white);
    letter-spacing: 0.5px;
  }
  /* front side */
  .card-front {
    left: 555px;
    top: 470px;
    background: var(--card-white);
  }
  .front-top {
    position: absolute; left: 0; top: 0; width: 100%; height: 128px;
    background: var(--card-white);
  }
  .front-brand {
    position: absolute; left: 175px; top: 38px;
    display: flex; flex-direction: column; align-items: flex-start;
  }
  .front-brand .brand-row { display: flex; align-items: center; gap: 10px; }
  .front-brand .mark-dot {
    width: 26px; height: 26px; border-radius: 50%;
    background: var(--brand-blue);
  }
  .front-brand .wordmark {
    font-family: "Oswald", Impact, sans-serif;
    font-weight: 700;
    font-size: 36px;
    line-height: 1;
    color: var(--brand-blue);
  }
  .front-brand .tagline {
    font-family: "Oswald", Impact, sans-serif;
    font-weight: 700;
    font-size: 11px;
    color: var(--brand-orange);
    letter-spacing: 0.3px;
    margin-top: 4px;
    margin-left: 36px;
  }
  .front-contact-band {
    position: absolute; left: 0; top: 128px; width: 100%; height: 100px;
    background: var(--brand-blue);
    color: var(--text-white);
  }
  .contact-list {
    position: absolute; left: 20px; top: 20px; width: 270px;
    list-style: none; text-align: right; font-size: 14px;
  }
  .contact-list li {
    display: flex; justify-content: flex-end; align-items: center; gap: 8px;
    margin-bottom: 8px;
  }
  .contact-list svg { width: 12px; height: 12px; flex: none; }
  .person {
    position: absolute; left: 322px; top: 14px;
  }
  .person .name { font-weight: 700; font-size: 16px; letter-spacing: 0.3px; }
  .person .role { font-size: 13px; margin-left: 10px; }
  .front-address-band {
    position: absolute; left: 0; top: 228px; width: 100%; height: 72px;
    background: var(--brand-orange);
    color: var(--text-white);
    display: flex; align-items: center; justify-content: center;
    font-size: 16px;
  }
</style>
</head>
<body>
  <section class="card card-back" aria-label="Card back">
    <span class="mark-dot"></span>
    <span class="wordmark">RAVEL CONSULTING</span>
  </section>

  <section class="card card-front" aria-label="Card front">
    <div class="front-top">
      <div class="front-brand">
        <div class="brand-row">
          <span class="mark-dot"></span>
          <span class="wordmark">RAVEL CONSULTING</span>
        </div>
        <span class="tagline">PLUMBING &amp; FIRE PROTECTION ENGINEERING</span>
      </div>
    </div>

    <div class="front-contact-band">
      <ul class="contact-list">
        <li>201-486-2713
          <svg viewBox="0 0 24 24" aria-hidden="true"><path fill="#fff" d="M6.6 10.8a15 15 0 0 0 6.6 6.6l2.2-2.2c.3-.3.7-.4 1-.2 1.1.4 2.3.6 3.6.6.6 0 1 .4 1 1V20c0 .6-.4 1-1 1A17 17 0 0 1 3 4c0-.6.4-1 1-1h3.5c.6 0 1 .4 1 1 0 1.3.2 2.5.6 3.6.1.3 0 .7-.2 1z"/></svg>
        </li>
        <li>ravelpipework@ravelmail.example
          <svg viewBox="0 0 24 24" aria-hidden="true"><path fill="#fff" d="M2 5h20v14H2z"/><path fill="none" stroke="#1565b0" stroke-width="2" d="M2 6l10 7 10-7"/></svg>
        </li>
      </ul>
      <div class="person">
        <div class="name">MARTIN KOLBECK</div>
        <div class="role">President</div>
      </div>
    </div>

    <div class="front-address-band">52-07 Danforth Street, Harlow Glen, HG 07563</div>
  </section>
</body>
</html>
```